Packaging design for Prenatal, Fish Oil, and Joint Pain product

We are looking for package design (label and outer box) for following products:
1) Merosa
- Product name: Merosa
- Benefit: Prenatal
- Feature DHA + Folic Acid
- What we need from you? We need box concept
- Box dimension 55mm Height x 145mm length x 100mm width
2) Omega 3 Alaskan Salmon
- Product name: Omega 3 Alaskan Salmon
- Benefit: Cognitive , cardiovascular Health, Joint Health, High cholesterol
- Feature: Alaskan Salmon
- What we need from you? We need label concept
- Label dimension: 60mm Height x 180mm Length
2) Ubrax
- Product name: Ubrax
- Benefit: Joint Health
- Feature: Glucosamin, Chondroitin, MSM
Designer can use generic text on other vitamin products for formula, usage instruction etc.
We have logo. The logo must be integrated in the packaging design. (please see attachment)

```html
<!DOCTYPE html>
<html lang="en">
<head>
<meta charset="utf-8">
<title>Merosa Prenatal – Box Dieline</title>
<link rel="stylesheet" href="https://fonts.googleapis.com/css2?family=Jost:wght@400;500&display=swap">
<style>
  :root {
    --page: #ffffff;
    --cut-line: #d9dcdc;
    --panel: #ffffff;
    --mint: #9fd4ba;
    --mint-light: #bfe6d2;
    --title-green: #3f8f6c;
    --body-ink: #2a2a2a;
    --brand-red: #d2302a;
    --white: #ffffff;
  }
  html, body {
    margin: 0;
    padding: 0;
    width: 1200px;
    height: 900px;
    overflow: hidden;
    background: var(--page);
  }
  .dieline {
    display: block;
    width: 1200px;
    height: 900px;
    font-family: "Jost", "Futura", sans-serif;
  }
  .sheet-frame { fill: none; stroke: #ececec; stroke-width: 1; }
  .cut { fill: var(--panel); stroke: var(--cut-line); stroke-width: 1; }
  .cut-mint { fill: var(--mint); stroke: var(--cut-line); stroke-width: 1; }
  .fold { stroke: var(--cut-line); stroke-width: 1; fill: none; }
  .benefit { fill: var(--title-green); font-size: 28px; font-weight: 400; letter-spacing: 0.5px; }
  .feature { fill: var(--body-ink); font-size: 11.5px; font-weight: 400; }
  .product-name { fill: var(--white); font-size: 29px; font-weight: 400; letter-spacing: 0.5px; }
  .brand { fill: var(--brand-red); font-weight: 500; }
  .brand-small { font-size: 20px; }
  .brand-large { font-size: 38px; }
</style>
</head>
<body>
<svg class="dieline" viewBox="0 0 1200 900" xmlns="http://www.w3.org/2000/svg">
  <defs>
    <radialGradient id="arc-glow" cx="590" cy="640" r="380" gradientUnits="userSpaceOnUse"
                    gradientTransform="translate(0 640) scale(1 0.62) translate(0 -640)">
      <stop offset="0" stop-color="var(--mint-light)" stop-opacity="1"/>
      <stop offset="0.55" stop-color="var(--mint-light)" stop-opacity="0.85"/>
      <stop offset="0.85" stop-color="var(--mint-light)" stop-opacity="0.35"/>
      <stop offset="1" stop-color="var(--mint-light)" stop-opacity="0"/>
    </radialGradient>
    <clipPath id="body-panels">
      <rect x="213" y="278" width="756" height="354"/>
    </clipPath>
  </defs>

  <rect class="sheet-frame" x="0.5" y="48.5" width="1199" height="813"/>

  <!-- top tuck flap and lid -->
  <path class="cut" d="M237 120 H433 L457 145 H213 Z"/>
  <rect class="cut" x="213" y="145" width="244" height="133"/>

  <!-- dust flaps -->
  <path class="cut" d="M457 278 V262 Q462 252 464 230 L475 162 Q478 145 495 145 H591 V278 Z"/>
  <path class="cut" d="M835 278 V145 H935 Q950 145 952 162 L960 245 Q962 262 969 268 V278 Z"/>

  <!-- body panels -->
  <rect class="cut" x="213" y="278" width="244" height="354"/>
  <rect class="cut" x="457" y="278" width="134" height="354"/>
  <rect class="cut" x="591" y="278" width="244" height="354"/>
  <rect class="cut" x="835" y="278" width="134" height="354"/>
  <path class="cut" d="M969 278 L993 288 V622 L969 632 Z"/>

  <!-- halftone arc decoration -->
  <g role="img" aria-label="Soft mint halftone dot arc rising behind the panels" clip-path="url(#body-panels)">
    <ellipse cx="590" cy="640" rx="380" ry="236" fill="url(#arc-glow)"/>
  </g>
  <line class="fold" x1="457" y1="278" x2="457" y2="632"/>
  <line class="fold" x1="591" y1="278" x2="591" y2="632"/>
  <line class="fold" x1="835" y1="278" x2="835" y2="632"/>
  <line class="fold" x1="969" y1="278" x2="969" y2="632"/>

  <!-- figure area -->
  <rect role="img" aria-label="White silhouette of a standing expectant mother"
        x="630" y="455" width="82" height="177" rx="30" fill="var(--white)" fill-opacity="0.75"/>

  <!-- bottom panels -->
  <path class="cut-mint" d="M457 632 H591 V766 H457 V766 L457 766 H578 Q572 750 575 735 L578 690 Q580 640 591 632 Z"/>
  <path class="cut-mint" d="M457 632 H591 L591 640 Q578 650 576 700 L573 740 Q572 760 582 766 H457 Z"/>
  <rect class="cut-mint" x="591" y="632" width="244" height="134"/>
  <path class="cut-mint" d="M591 766 H835 L811 790 H615 Z"/>
  <path class="cut-mint" d="M835 632 H969 V766 H858 Q850 760 850 745 L846 690 Q844 645 835 640 Z"/>

  <!-- lid brand (upside down) -->
  <text class="brand brand-small" x="335" y="210" text-anchor="middle" transform="rotate(180 335 210)">Novela</text>

  <!-- back panel copy -->
  <text class="benefit" x="336" y="364" text-anchor="middle">Prenatal</text>
  <text class="feature" x="335" y="423" text-anchor="middle">Feature DHA + Folic Acid</text>
  <text class="product-name" x="385" y="609" text-anchor="middle">Merosa</text>

  <!-- front panel copy -->
  <text class="benefit" x="713" y="351" text-anchor="middle">Prenatal</text>
  <text class="feature" x="712" y="410" text-anchor="middle">Feature DHA + Folic Acid</text>
  <text class="product-name" x="767" y="609" text-anchor="middle">Merosa</text>

  <!-- side brand marks -->
  <text class="brand brand-small" x="524" y="605" text-anchor="middle">Novela</text>
  <text class="brand brand-small" x="900" y="605" text-anchor="middle">Novela</text>

  <!-- bottom brand mark -->
  <text class="brand brand-large" x="712" y="722" text-anchor="middle">Novela</text>
</svg>
</body>
</html>
```